Creative, fresh business card design for Orrin Linings

We need a fresh, creative business card design for Orrin Linings. We are the manufacturer of Orrin Linings in Australia. Wall panels are 2400 x 1200mm panels made from MDF and feature 3D patterns on the face of the panel. The colours to be used are green, silver/grey and white RGB
Red 187
Green 207
Blue 65.

An idea is to possibly use a watermark of one of our designs as a background (like on the "Ferns" design on the left hand side of page 2 of our brochure).

Target Market(s)

Interior designers, architects, builders and home renovators

Industry/Entity Type

Business

Contact Information for Business Card

Details to go on the card are:
Our logo (attached),
Slogan: "Decorative panels for interiors and exteriors",
Contact name,
Position,
Mobile phone number,
Business address,
Business phone,
Business fax,
Website and
Email address.

I have attached a few images of our panels and our brochure for reference.

The colours of the business card should feature our logo colours which are: RGB
Red 187
Green 207
Blue 65

Requirements
Must have
• Very modern fonts and design. Some of the designs shown especially the "Weave" design which is a popular design.
Nice to have
• Creative but simple design. Very contemporary.
Should not have
• Anything ornate or old fashioned.

```html
<!DOCTYPE html>
<html lang="en">
<head>
<meta charset="utf-8">
<title>Orrin Linings — Business Cards</title>
<link rel="stylesheet" href="https://fonts.googleapis.com/css2?family=Lato:wght@400;700&display=swap">
<style>
  :root {
    --green: rgb(187, 207, 65);
    --grey: #848488;
    --grey-text: #7a7a7e;
    --white: #ffffff;
    --stage: #2e2e30;
    --dark-wave-a: #3f3f42;
    --dark-wave-b: #d9d9d9;
    --light-wave-a: #e4e4e4;
    --light-wave-b: #fbfbfb;
  }
  * { box-sizing: border-box; margin: 0; padding: 0; }
  html, body { width: 1200px; height: 900px; overflow: hidden; }
  body {
    background: var(--stage);
    font-family: "Lato", Arial, sans-serif;
    position: relative;
  }
  .card {
    position: absolute;
    width: 514px;
    height: 296px;
    background: var(--white);
    box-shadow: 0 2px 8px rgba(0,0,0,0.45);
  }
  .card--front-dark  { left: 72px;  top: 138px; }
  .card--back-dark   { left: 615px; top: 138px; }
  .card--front-light { left: 72px;  top: 464px; }
  .card--back-light  { left: 615px; top: 464px; }

  .texture { position: absolute; }
  .texture--dark  { background: linear-gradient(160deg, var(--dark-wave-a) 0%, #8a8a8c 45%, var(--dark-wave-b) 100%); }
  .texture--light { background: linear-gradient(160deg, var(--light-wave-a) 0%, var(--light-wave-b) 55%, var(--light-wave-a) 100%); }

  .front-texture { left: 22px; top: 22px; width: 470px; height: 252px; }

  .brand {
    position: absolute;
    display: flex;
    align-items: center;
    gap: 10px;
    font-weight: 700;
    white-space: nowrap;
  }
  .brand__mark { width: 18px; height: 18px; background: var(--green); flex: none; }
  .brand--front {
    left: 50%; top: 50%;
    transform: translate(-50%, -50%);
    font-size: 34px;
  }
  .brand--on-dark  { color: var(--white); }
  .brand--on-light { color: var(--grey-text); }

  .person {
    position: absolute;
    left: 22px; top: 22px;
    width: 167px; height: 132px;
    background: var(--grey);
    color: var(--white);
    padding: 14px 19px;
    font-size: 13px;
    line-height: 18px;
  }
  .person__name { font-weight: 700; }
  .person__mobile { margin-top: 16px; }
  .person__mobile b { font-weight: 700; }

  .back-texture { left: 194px; top: 22px; width: 298px; height: 132px; }

  .brand-cell {
    position: absolute;
    left: 22px; top: 160px;
    width: 167px; height: 97px;
    display: flex; align-items: center; justify-content: center;
  }
  .brand--back {
    position: static;
    gap: 7px;
    font-size: 19px;
    color: var(--grey-text);
  }
  .brand--back .brand__mark { width: 14px; height: 14px; }

  .contact {
    position: absolute;
    left: 194px; top: 160px;
    width: 298px; height: 97px;
    background: var(--green);
    color: var(--white);
    padding: 12px 11px;
    font-size: 13px;
    line-height: 19px;
    white-space: nowrap;
  }
  .contact b { font-weight: 700; }

  .slogan {
    position: absolute;
    right: 22px; top: 268px;
    font-size: 14px;
    letter-spacing: 2.9px;
    color: var(--grey-text);
    white-space: nowrap;
  }
</style>
</head>
<body>

  <!-- Dark edition: front -->
  <section class="card card--front-dark">
    <div class="texture texture--dark front-texture" role="img" aria-label="Photograph of a dark grey wave-patterned 3D wall panel"></div>
    <div class="brand brand--front brand--on-dark"><span class="brand__mark"></span>Orrin Linings</div>
  </section>

  <!-- Dark edition: back -->
  <section class="card card--back-dark">
    <div class="person">
      <p class="person__name">Callum Reyes</p>
      <p>managing director</p>
      <p class="person__mobile">M <b>04 1200 3400</b></p>
    </div>
    <div class="texture texture--dark back-texture" role="img" aria-label="Photograph of a dark grey wave-patterned 3D wall panel"></div>
    <div class="brand-cell">
      <div class="brand brand--back"><span class="brand__mark"></span>Orrin Linings</div>
    </div>
    <div class="contact">
      <p>P <b>02 9100 0142</b>&nbsp; F <b>02 9100 0143</b></p>
      <p>14 Kestrel Road, Marlow Vale NSW 2990</p>
      <p>sales@orrinlinings.com.au</p>
      <p><b>www.orrinlinings.com.au</b></p>
    </div>
    <p class="slogan">decorative panels for interiors &amp; exteriors</p>
  </section>

  <!-- Light edition: front -->
  <section class="card card--front-light">
    <div class="texture texture--light front-texture" role="img" aria-label="Photograph of a white wave-patterned 3D wall panel"></div>
    <div class="brand brand--front brand--on-light"><span class="brand__mark"></span>Orrin Linings</div>
  </section>

  <!-- Light edition: back -->
  <section class="card card--back-light">
    <div class="person">
      <p class="person__name">Callum Reyes</p>
      <p>managing director</p>
      <p class="person__mobile">M <b>04 1200 3400</b></p>
    </div>
    <div class="texture texture--light back-texture" role="img" aria-label="Photograph of a white wave-patterned 3D wall panel"></div>
    <div class="brand-cell">
      <div class="brand brand--back"><span class="brand__mark"></span>Orrin Linings</div>
    </div>
    <div class="contact">
      <p>P <b>02 9100 0142</b>&nbsp; F <b>02 9100 0143</b></p>
      <p>14 Kestrel Road, Marlow Vale NSW 2990</p>
      <p>sales@orrinlinings.com.au</p>
      <p><b>www.orrinlinings.com.au</b></p>
    </div>
    <p class="slogan">decorative panels for interiors &amp; exteriors</p>
  </section>

</body>
</html>
```